Oversized( 8.52 by 4.57) handout postcards.
We need promotional post cards that our congregation can use to pass out to their frineds and family for a special Easter Week Awakening. I attempted to create "something" but was not completely satisfied with it. I have included my attempt in the uploaded images.
Trhe front part of the post card I would like for it to capture the attention of people. The Backside of the postcard can contain event information.
About the Event Information.
Easter Week Awakening
Special Guest: Dale Wickersham (www.dalewickersham-example.com)
Dates: Sunday March 15 thru Wednesday March 18
Times: Sunday 9:00 a.m., 11:00 a.m., and 6:00 p.m.
Monday - Wednesday 6:00 p.m. with a free meal being served at 5:00 p.m.
Our Location is 418 N. Marlow Street, Brookhaven Falls, WS 00147
Our Phone Number 620-555-0147

```html
<!DOCTYPE html>
<html lang="en">
<head>
<meta charset="utf-8">
<title>Easter Week Awakening 2015</title>
<link rel="stylesheet" href="https://fonts.googleapis.com/css2?family=Oswald:wght@400;500;700&family=Roboto+Condensed:wght@700&display=swap">
<style>
  :root {
    --ink: #0b0b0b;
    --white: #ffffff;
    --tan: #d9cba3;
    --red: #e0262b;
    --sky: #6fc3e8;
    --stone: #8f8b78;
    --stone-light: #b9b49f;
    --logo-grey: #bdbdbd;
  }
  html, body {
    margin: 0;
    padding: 0;
    width: 1200px;
    height: 771px;
    overflow: hidden;
    background: var(--white);
  }
  .postcard {
    position: relative;
    width: 1200px;
    height: 771px;
    overflow: hidden;
    background: linear-gradient(135deg, var(--stone-light), var(--stone));
    font-family: "Oswald", sans-serif;
  }
  .speaker-photo {
    position: absolute;
    left: 0;
    top: 0;
    width: 700px;
    height: 771px;
    background:
      radial-gradient(ellipse at 30% 55%, #b7b0a2 0%, rgba(183,176,162,0) 45%),
      linear-gradient(180deg, #4a4b3a 0%, #6b6a4d 35%, #7e9256 60%, #3d5a7a 100%);
  }
  .info-panel {
    position: absolute;
    left: 0;
    top: 0;
    width: 1200px;
    height: 771px;
  }
  .event-title {
    position: absolute;
    left: 24px;
    top: 12px;
    margin: 0;
    line-height: 1;
    font-weight: 700;
    text-transform: uppercase;
  }
  .event-title span { display: block; }
  .title-lead { color: var(--white); font-size: 34px; letter-spacing: 0.5px; }
  .title-main { color: var(--red); font-size: 34px; letter-spacing: 1px; margin-top: 4px; }
  .title-year { color: var(--sky); font-size: 44px; letter-spacing: 10px; margin-top: 2px; font-weight: 400; }
  .dates {
    position: absolute;
    left: 580px;
    top: 50px;
    margin: 0;
    color: var(--white);
    font-family: "Roboto Condensed", sans-serif;
    font-weight: 700;
    font-size: 54px;
    line-height: 62px;
    letter-spacing: -0.5px;
    white-space: nowrap;
  }
  .schedule {
    position: absolute;
    right: 134px;
    top: 198px;
    text-align: right;
    color: var(--tan);
    text-transform: uppercase;
  }
  .schedule h3 {
    margin: 0;
    font-weight: 500;
    font-size: 36px;
    line-height: 44px;
  }
  .schedule p {
    margin: 10px 0 0;
    font-weight: 400;
    font-size: 23px;
    line-height: 40px;
    letter-spacing: 0.4px;
  }
  .schedule .block + .block { margin-top: 22px; }
  .church-name {
    position: absolute;
    left: 660px;
    top: 548px;
    width: 180px;
    color: var(--logo-grey);
    font-weight: 400;
    font-size: 34px;
    line-height: 40px;
    text-transform: uppercase;
  }
  .contact {
    position: absolute;
    left: 858px;
    top: 536px;
    color: var(--white);
    font-style: normal;
    font-weight: 400;
    font-size: 23px;
    line-height: 46px;
    letter-spacing: 0.3px;
    text-transform: uppercase;
    white-space: nowrap;
  }
  .contact p { margin: 0; }
  .guest {
    position: absolute;
    left: 48px;
    top: 596px;
    width: 470px;
    text-align: center;
    text-transform: uppercase;
  }
  .guest-label {
    margin: 0;
    color: var(--white);
    font-weight: 700;
    font-size: 44px;
    line-height: 52px;
  }
  .guest-name {
    margin: 0;
    color: var(--red);
    font-weight: 700;
    font-size: 56px;
    line-height: 64px;
    letter-spacing: 0.5px;
  }
  .guest-site {
    margin: 0;
    color: var(--red);
    font-weight: 400;
    font-size: 19px;
    line-height: 24px;
    text-transform: lowercase;
    letter-spacing: 1px;
  }
</style>
</head>
<body>
  <main class="postcard">
    <div class="speaker-photo" role="img" aria-label="Photo of the guest speaker seated outdoors in prayer, hands clasped, with autumn trees and grass behind him"></div>

    <svg class="info-panel" viewBox="0 0 1200 771" aria-hidden="true">
      <path fill="var(--ink)" d="M600 0 H1200 V22 L1178 40 L1186 90 L1166 140 L1176 210 L1160 280 L1172 360 L1150 430 L1168 500 L1146 560 L1160 630 L1132 690 L1140 740 L1110 771 H640 L612 740 L624 690 L596 640 L580 560 L598 500 L570 440 L586 360 L562 300 L578 230 L556 170 L572 110 L552 50 Z"/>
    </svg>

    <h1 class="event-title">
      <span class="title-lead">Easter Week</span>
      <span class="title-main">Awakening</span>
      <span class="title-year">2015</span>
    </h1>

    <h2 class="dates">Sunday March 15 through<br>Wednesday March 18</h2>

    <section class="schedule">
      <div class="block">
        <h3>Sunday</h3>
        <p>9:00 A.M., 11:00 A.M., and 6:00 P.M.</p>
      </div>
      <div class="block">
        <h3>Monday-Wednesday</h3>
        <p>6:00 P.M. with a free meal being<br>served at 5:00 P.M.</p>
      </div>
    </section>

    <div class="church-name">Marlow Street Church</div>

    <address class="contact">
      <p>418 N. Marlow Street</p>
      <p>Brookhaven Falls, WS 00147</p>
      <p>(620)-555-0147</p>
    </address>

    <section class="guest">
      <p class="guest-label">Special Guest</p>
      <p class="guest-name">Dale Wickersham</p>
      <p class="guest-site">www.dalewickersham-example.com</p>
    </section>
  </main>
</body>
</html>
```